Birchwell Craft House business card design- Fine Art sculpture business (Contract guaranteed)

This business card is for a fine art business. Though we don't have a website up and running yet it should be up soon. I would like the business card to be elegant and fairly simple with a picture of one of my sculptures on the front (you might need to photoshop out the background) as well as my basic contact info (my name,phone # and e-mail). On the back I'd like it to be pretty simple with just "Notes" and some blank lines for writing in info.
Updates

Target Market(s)

High end artwork buyers

Industry/Entity Type

Art Gallery

Contact Information for Business Card

Wendell Marsh Phone: (555) 312-4098 E-mail: wendell@quarrymint.example Facebook: @birchwellcrafthouse Instagram: birchwellcrafthouse

Colors

Designer to choose colors to be used in the design.

Requirements
Must have
• *A picture of one of my sculptures*, my name, business name (Birchwell Craft House), e-mail, phone #, and a notes section on the back.
• Birchwell Craft House
• Wendell Marsh
• (555)312-4098
• wendell@quarrymint.example
• Facebook: @birchwellcrafthouse
• Instagram: birchwellcrafthouse
Nice to have
• It'd be nice if you can crop out the background in the sculpture pictures, which ever one you end up using.

```html
<!DOCTYPE html>
<html lang="en">
<head>
<meta charset="utf-8">
<title>Birchwell Craft House – Business Card</title>
<link href="https://fonts.googleapis.com/css2?family=Ubuntu:wght@300;400&family=Arimo:wght@400;700&family=Tinos&display=swap" rel="stylesheet">
<style>
  :root {
    --rust: #b84b25;
    --ink: #141414;
    --paper: #ffffff;
    --name-grey: #d6d6d6;
    --stage: #ece9e6;
    --agate-dark: #3a2a26;
    --agate-mid: #7a5a4c;
    --agate-light: #c9a88f;
  }
  * { margin: 0; padding: 0; box-sizing: border-box; }
  html, body { width: 1200px; height: 1000px; overflow: hidden; }
  body { background: var(--stage); position: relative; font-family: "Arimo", Arial, sans-serif; }

  .card {
    position: absolute;
    width: 560px;
    height: 320px;
    overflow: hidden;
    box-shadow: 0 4px 14px rgba(0,0,0,0.18);
  }

  /* Back: notes side */
  .card-back { left: 70px; top: 110px; background: var(--rust); }
  .card-back .studio-title {
    position: absolute; top: 22px; left: 0; width: 100%;
    text-align: center;
    font-family: "Ubuntu", sans-serif;
    font-weight: 400;
    font-size: 30px; color: var(--paper); letter-spacing: 0.5px;
  }
  .note-lines { position: absolute; left: 60px; right: 60px; top: 92px; }
  .note-line { height: 1px; background: var(--ink); margin-bottom: 34px; }
  .contact-band {
    position: absolute; left: 0; bottom: 0; width: 100%; height: 72px;
    background: var(--ink);
  }
  .band-rule {
    position: absolute; top: -6px; height: 3px; background: var(--paper);
  }
  .band-rule.left { left: 0; width: 49%; }
  .band-rule.right { right: 0; width: 49%; }
  .contact-item {
    position: absolute; top: 18px; display: flex; align-items: center; gap: 10px;
    color: var(--paper); font-size: 15px; white-space: nowrap;
  }
  .contact-item.phone { left: 24px; }
  .contact-item.email { left: 282px; }
  .contact-icon { width: 36px; height: 36px; flex: none; }

  /* Front: name side */
  .card-front { left: 570px; top: 560px; background: var(--rust); }
  .card-front .backdrop { position: absolute; inset: 0; }
  .sculpture-photo {
    position: absolute; left: 300px; top: 22px; width: 110px; height: 260px;
    background: linear-gradient(160deg, var(--agate-light) 0%, var(--agate-mid) 35%, var(--agate-dark) 70%, #1e1a18 100%);
    border-radius: 50% 40% 20% 30% / 60% 50% 20% 20%;
  }
  .owner-name {
    position: absolute; left: 70px; top: 232px;
    font-weight: 700; font-size: 26px; color: var(--name-grey);
  }
  .owner-studio {
    position: absolute; left: 104px; top: 266px;
    font-family: "Tinos", serif; font-size: 19px; color: var(--rust);
  }
</style>
</head>
<body>

  <section class="card card-back" aria-label="Card back – notes side">
    <h1 class="studio-title">Birchwell Craft House</h1>
    <div class="note-lines">
      <div class="note-line"></div>
      <div class="note-line"></div>
      <div class="note-line"></div>
      <div class="note-line"></div>
    </div>
    <div class="contact-band">
      <span class="band-rule left"></span>
      <span class="band-rule right"></span>
      <div class="contact-item phone">
        <svg class="contact-icon" viewBox="0 0 36 36" aria-hidden="true">
          <circle cx="18" cy="18" r="16" fill="none" stroke="var(--rust)" stroke-width="1.5"/>
          <path d="M11 14c0-2 2-3 3-3l2 3-2 2c1 2 3 4 5 5l2-2 3 2c0 1-1 3-3 3-6 0-10-4-10-10z" fill="none" stroke="var(--rust)" stroke-width="1.4"/>
        </svg>
        <span>+555 312-4098</span>
      </div>
      <div class="contact-item email">
        <svg class="contact-icon" viewBox="0 0 36 36" aria-hidden="true">
          <circle cx="18" cy="18" r="16" fill="none" stroke="var(--rust)" stroke-width="1.5"/>
          <rect x="10" y="12" width="16" height="12" fill="none" stroke="var(--rust)" stroke-width="1.4"/>
          <path d="M10 12l8 7 8-7" fill="none" stroke="var(--rust)" stroke-width="1.4"/>
        </svg>
        <span>wendell@quarrymint.example</span>
      </div>
    </div>
  </section>

  <section class="card card-front" aria-label="Card front – name side">
    <svg class="backdrop" viewBox="0 0 560 320" preserveAspectRatio="none" aria-hidden="true">
      <ellipse cx="280" cy="160" rx="250" ry="215" fill="var(--ink)"/>
    </svg>
    <div class="sculpture-photo" role="img" aria-label="Photograph of a polished agate slice sculpture on a small stone base"></div>
    <p class="owner-name">Wendell Marsh</p>
    <p class="owner-studio">Birchwell Craft House</p>
  </section>

</body>
</html>
```